I'm looking for a smart new design for business cards

Industry/Entity Type

Commercial Electrical

Contact Information for Business Card

Logo, name, email, position, website QR

Requirements
Nice to have
• Logo embedded behind the text side

```html
<!DOCTYPE html>
<html lang="en">
<head>
<meta charset="utf-8">
<title>Kestrel Power Co – Business Card</title>
<link rel="stylesheet" href="https://fonts.googleapis.com/css2?family=Montserrat:wght@700;800&family=Arimo:wght@400&display=swap">
<style>
  :root {
    --page: #e4e4e4;
    --navy: #12169a;
    --navy-deep: #0b0f6e;
    --blue-bright: #2d3cf2;
    --red: #e4002b;
    --white: #ffffff;
    --ink: #111111;
  }
  * { margin: 0; padding: 0; box-sizing: border-box; }
  html, body {
    width: 1200px; height: 1200px; overflow: hidden;
    background: var(--page);
  }
  .canvas { position: relative; width: 1200px; height: 1200px; }

  .card {
    position: absolute; left: 256px;
    width: 688px; height: 394px;
    border-radius: 22px; overflow: hidden;
  }
  .card--front { top: 150px; background: var(--white); }
  .card--back  { top: 650px; background: var(--navy); }

  .front-art { position: absolute; inset: 0; width: 100%; height: 100%; }

  .brand {
    position: absolute; left: 48px; top: 74px;
    display: flex; align-items: center; gap: 9px;
  }
  .brand__mark { width: 14px; height: 14px; background: var(--red); }
  .brand__name {
    font-family: "Montserrat", sans-serif; font-weight: 800;
    font-size: 18px; letter-spacing: 0.3px; color: var(--navy);
    text-transform: uppercase; white-space: nowrap;
  }

  .person {
    position: absolute; right: 50px; top: 44px; text-align: right;
    color: var(--white);
  }
  .person__name {
    font-family: "Montserrat", sans-serif; font-weight: 800;
    font-size: 26px; letter-spacing: 0.3px; line-height: 1.2;
    white-space: nowrap;
  }
  .person__role {
    font-family: "Arimo", sans-serif; font-size: 15px; margin-top: 2px;
  }

  .contact {
    position: absolute; right: 45px; top: 234px; text-align: right;
    font-family: "Arimo", sans-serif; color: var(--white);
  }
  .contact__address { font-size: 16.5px; line-height: 21px; padding-right: 5px; }
  .contact__list { list-style: none; margin-top: 6px; font-size: 16.5px; }
  .contact__item {
    display: flex; justify-content: flex-end; align-items: center;
    gap: 14px; height: 20px;
  }
  .contact__icon { width: 13px; height: 13px; flex: none; }
  .contact__web { font-size: 16.5px; margin-top: 4px; }

  .pattern {
    position: absolute; inset: 0;
    background: linear-gradient(100deg, var(--navy-deep) 0%, var(--navy) 45%, var(--blue-bright) 100%);
    opacity: 0.9;
  }
  .back-brand {
    position: absolute; left: 532px; top: 287px;
    font-family: "Montserrat", sans-serif; font-weight: 800;
    font-size: 20px; color: var(--white); letter-spacing: 0.5px;
  }
</style>
</head>
<body>
<main class="canvas">

  <section class="card card--front" aria-label="Business card front">
    <svg class="front-art" viewBox="0 0 802 458" preserveAspectRatio="none" aria-hidden="true">
      <polygon fill="var(--navy)" points="553,0 802,0 802,458 316,458 534,202 440,202"/>
      <polygon fill="var(--red)" stroke="var(--white)" stroke-width="2"
               points="446,0 553,0 440,202 534,202 310,458 430,245 303,245"/>
    </svg>

    <div class="brand">
      <span class="brand__mark"></span>
      <span class="brand__name">Kestrel Power Co</span>
    </div>

    <div class="person">
      <p class="person__name">DAN REEVES</p>
      <p class="person__role">President</p>
    </div>

    <div class="contact">
      <p class="contact__address">1420 Harbour Street<br>Wellington Park, 30218</p>
      <ul class="contact__list">
        <li class="contact__item">555-210-4187
          <svg class="contact__icon" viewBox="0 0 16 16" aria-hidden="true"><path fill="none" stroke="var(--red)" stroke-width="2" d="M3 2l3 0 1 4-2 1c1 2 2 3 4 4l1-2 4 1 0 3c-7 0-11-4-11-11z"/></svg>
        </li>
        <li class="contact__item">555-210-4920
          <svg class="contact__icon" viewBox="0 0 16 16" aria-hidden="true"><rect x="4" y="1" width="8" height="14" rx="1.5" fill="none" stroke="var(--red)" stroke-width="1.8"/></svg>
        </li>
        <li class="contact__item">hello@kestrelpower.com
          <svg class="contact__icon" viewBox="0 0 16 16" aria-hidden="true"><rect x="1" y="3" width="14" height="10" fill="var(--red)"/><path d="M1 3l7 6 7-6" fill="none" stroke="var(--navy)" stroke-width="1.2"/></svg>
        </li>
      </ul>
      <p class="contact__web">www.kestrelpower.com</p>
    </div>
  </section>

  <section class="card card--back" aria-label="Business card back">
    <div class="pattern" role="img" aria-label="Repeating tone-on-tone brand pattern fading from dark navy to bright blue"></div>
    <p class="back-brand">KESTREL</p>
  </section>

</main>
</body>
</html>
```